Vessa Kliniq - Dermatology Consultation App

Vessa Kliniq is launching a new Pindle IOS App for online Dermatology consultation. We would appreciate a simple Scandinavian design which communicates trust, comfort and expensive feel. Most yacht designs have similar color palette, light wood colors and textures, but don’t be restricted by those in your artistic search.
The process is completed in three easy steps:
1. take a Snapshot.
2. Describe and Send it.
3. get Diagnosis and Treatment.
The Home screen should also have buttons - Start new Case, Follow up Visit, Rx Refill.
15% of the Home screen should also have a field/button - Medical Cosmetics Shop.
10% of the Home screen should also have a field or buttons for Our Partners (sponsors) – Lumavel, Norvexa, Toral, Ostra. (if you click you would be directed to their sites)
Note / Suggestion : Maybe you could use a larger picture of a dermatologist and have overlying fields and content, just for more influencing effect. (I am not a professional though)
Thank you so much.
24 - 59 Female
Club

```html
<!DOCTYPE html>
<html lang="en">
<head>
<meta charset="utf-8">
<title>Vessa Kliniq – Case Detail</title>
<link rel="stylesheet" href="https://fonts.googleapis.com/css2?family=Roboto:wght@400&family=Roboto+Condensed:wght@300;400&display=swap">
<style>
  :root {
    --page-bg: #d9ccb9;
    --screen-bg: #ffffff;
    --ink: #5b5654;
    --ink-soft: #847d7a;
    --ink-faint: #c8c2bf;
    --accent: #dcb79a;
    --tab-bg: #f3f0ee;
    --badge: #ef4a4a;
    --photo-light: #fbf1e8;
    --photo-warm: #ecc6aa;
  }
  * { box-sizing: border-box; margin: 0; padding: 0; }
  html, body {
    width: 780px; height: 1200px; overflow: hidden;
    background: var(--page-bg);
  }
  .screen {
    position: absolute; left: 52px; top: 0;
    width: 676px; height: 1200px;
    background: var(--screen-bg);
    font-family: "Roboto Condensed", "Arial Narrow", sans-serif;
    color: var(--ink);
    overflow: hidden;
  }
  .status-bar {
    position: absolute; left: 0; top: 8px; width: 100%; height: 28px;
    font-family: "Roboto", Arial, sans-serif; font-size: 19px; color: var(--ink-soft);
  }
  .status-bar .carrier { position: absolute; left: 22px; top: 2px; display: flex; align-items: center; gap: 6px; }
  .status-bar .time { position: absolute; left: 0; right: 0; top: 2px; text-align: center; }
  .status-bar .power { position: absolute; right: 20px; top: 2px; display: flex; align-items: center; gap: 8px; }
  .back-link {
    position: absolute; left: 44px; top: 64px;
    font-size: 22px; color: #d6d1ce; letter-spacing: .5px;
    display: flex; align-items: center; gap: 8px; font-weight: 400;
  }
  .case-photo {
    position: absolute; left: 98px; top: 111px; width: 480px; height: 537px;
    background: linear-gradient(180deg, var(--photo-light) 0%, var(--photo-warm) 100%);
  }
  .partners {
    position: absolute; left: 40px; right: 40px; top: 688px;
    display: flex; justify-content: space-between; align-items: center;
    font-size: 30px; font-weight: 300; color: var(--ink-faint); letter-spacing: 1px;
  }
  .case-title {
    position: absolute; left: 0; right: 0; top: 765px; text-align: center;
    font-size: 38px; font-weight: 300; color: var(--ink);
  }
  .case-title-rule {
    position: absolute; left: 168px; width: 340px; top: 826px; height: 3px;
    background: var(--accent);
  }
  .case-description {
    position: absolute; left: 78px; right: 78px; top: 862px;
    text-align: center; font-size: 15px; line-height: 19.7px; color: var(--ink-soft);
    letter-spacing: .15px;
  }
  .send-button {
    position: absolute; left: 223px; top: 980px; width: 231px; height: 51px;
    border-radius: 26px; border: 1px solid #e3dfdc; background: #fff;
    box-shadow: 0 3px 3px rgba(0,0,0,.12);
    font: 400 19px "Roboto Condensed", sans-serif; color: var(--ink-soft);
    display: flex; align-items: center; justify-content: center;
  }
  .tab-bar {
    position: absolute; left: 0; bottom: 0; width: 100%; height: 102px;
    background: var(--tab-bg); display: flex;
  }
  .tab {
    flex: 1; position: relative; display: flex; flex-direction: column; align-items: center;
    padding-top: 12px; font-size: 12.5px; color: var(--ink-soft); letter-spacing: .2px;
  }
  .tab svg { height: 50px; width: 56px; margin-bottom: 12px; }
  .tab .badge {
    position: absolute; top: 8px; left: calc(50% + 16px);
    width: 18px; height: 18px; border-radius: 50%; background: var(--badge);
    color: #fff; font-size: 11px; line-height: 18px; text-align: center;
  }
</style>
</head>
<body>
<main class="screen">
  <header class="status-bar">
    <div class="carrier">
      <svg width="62" height="12" viewBox="0 0 62 12" fill="#7d7775" stroke="#7d7775">
        <circle cx="6" cy="6" r="5"/><circle cx="18" cy="6" r="5"/><circle cx="30" cy="6" r="5"/>
        <circle cx="42" cy="6" r="4.4" fill="none"/><circle cx="54" cy="6" r="4.4" fill="none"/>
      </svg>
      <span>Corvo</span>
      <svg width="20" height="16" viewBox="0 0 20 16" fill="none" stroke="#7d7775" stroke-width="2">
        <path d="M2 6a12 12 0 0 1 16 0M5 9.5a7 7 0 0 1 10 0"/><circle cx="10" cy="13" r="1.6" fill="#7d7775"/>
      </svg>
    </div>
    <div class="time">4:21 PM</div>
    <div class="power">
      <svg width="12" height="20" viewBox="0 0 12 20" fill="none" stroke="#b8b2af" stroke-width="1.5"><path d="M2 5l8 9-4 4V2l4 4-8 9"/></svg>
      <span>100%</span>
      <svg width="44" height="16" viewBox="0 0 44 16"><rect x="1" y="1" width="38" height="14" rx="2" fill="none" stroke="#7d7775"/><rect x="3" y="3" width="34" height="10" fill="#7d7775"/><rect x="40" y="5" width="3" height="6" fill="#7d7775"/></svg>
    </div>
  </header>

  <div class="back-link">
    <svg width="12" height="14" viewBox="0 0 12 14"><path d="M12 0v14L0 7z" fill="#d6d1ce"/></svg>
    BACK
  </div>

  <div class="case-photo" role="img" aria-label="Portrait photo of a woman with clear skin, hands resting on her cheeks"></div>

  <nav class="partners" aria-label="Our partners">
    <span>Ostra</span><span>TORAL</span><span>NORVEXA</span><span>Lumavel</span>
  </nav>

  <h1 class="case-title">Weird looking face mole</h1>
  <div class="case-title-rule"></div>

  <p class="case-description">Lorem ipsum dolor sit amet, duo nemore adipiscing interpretaris ea, et illum saepe iuvaret sit. Rebum assum id qui. Ad putant omittam urbanitas sed. Et est singulis reformidans, at oporteat legendos necessitatibus pro, ea officiis consulatu vim. Cu eos duis putant numquam, sanctus theophrastus sea ut.</p>

  <div class="send-button">SEND</div>

  <footer class="tab-bar">
    <div class="tab">
      <svg viewBox="0 0 56 50" fill="none" stroke="#8a8380" stroke-width="1.6">
        <rect x="12" y="6" width="26" height="40"/><rect x="19" y="3" width="12" height="6" fill="#f3f0ee"/>
        <path d="M17 16h16M17 22h16M17 28h16M17 34h16M17 40h10"/><path d="M43 20v22l-2 5-2-5V20z"/>
      </svg>
      START NEW CASE
    </div>
    <div class="tab">
      <svg viewBox="0 0 56 50" fill="none" stroke="#8a8380" stroke-width="1.6">
        <circle cx="28" cy="9" r="6"/><path d="M28 6v6M25 9h6"/>
        <path d="M8 46V18h40v28M4 46h48"/>
        <rect x="14" y="26" width="5" height="9"/><rect x="25.5" y="26" width="5" height="9"/><rect x="37" y="26" width="5" height="9"/>
      </svg>
      <span class="badge">2</span>
      FOLLOW UP VISITS
    </div>
    <div class="tab">
      <svg viewBox="0 0 56 50" fill="none" stroke="#8a8380" stroke-width="1.6">
        <rect x="14" y="3" width="28" height="44"/>
        <path d="M19 8v10M19 8h4a2.5 2.5 0 0 1 0 5h-4M22 13l5 6M27 14l-4 5"/>
        <path d="M19 26h18M19 32h18M19 38h18"/>
      </svg>
      MENU
    </div>
    <div class="tab">
      <svg viewBox="0 0 56 50" fill="none" stroke="#8a8380" stroke-width="1.6">
        <path d="M4 8h8l5 24h26l5-18H14M46 6l4-2"/><path d="M16 22h30M18 28h26"/>
        <circle cx="20" cy="40" r="3"/><circle cx="40" cy="40" r="3"/><path d="M17 32l2 5M43 32l-2 5"/>
      </svg>
      SHOP COSMETICS
    </div>
  </footer>
</main>
</body>
</html>
```